business cards

we want our logos on the back
the information on it are on the design I've uploaded
come up with whatever you think is best, we want something professional, sophisticated and sleek.

```html
<!DOCTYPE html>
<html lang="en">
<head>
<meta charset="utf-8">
<title>Crestline Health and Performance – Business Cards</title>
<link href="https://fonts.googleapis.com/css2?family=Montserrat:wght@400;500;700&display=swap" rel="stylesheet">
<style>
  :root {
    --bg: #1b1b1d;
    --card: #1f1f21;
    --card-edge: #262628;
    --green: #4fbf3f;
    --white: #f4f4f4;
    --grey: #d9d9d9;
  }
  * { box-sizing: border-box; margin: 0; padding: 0; }
  html, body { width: 1200px; height: 900px; overflow: hidden; }
  body {
    background: var(--bg);
    font-family: "Montserrat", sans-serif;
    color: var(--white);
    display: flex;
    flex-direction: column;
    align-items: center;
    justify-content: center;
    gap: 40px;
  }
  .card {
    position: relative;
    width: 620px;
    height: 378px;
    border-radius: 18px;
    background: linear-gradient(135deg, var(--card-edge), var(--card) 60%);
    overflow: hidden;
    box-shadow: 0 12px 30px rgba(0,0,0,.45);
  }
  .card__band {
    position: absolute;
    left: 0; right: 0; bottom: 0;
    height: 12px;
    background: var(--green);
  }
  /* Front */
  .card--front .brand {
    position: absolute;
    inset: 0 0 12px 0;
    display: flex;
    flex-direction: column;
    align-items: center;
    justify-content: center;
    gap: 16px;
  }
  .brand__name {
    display: flex;
    align-items: center;
    gap: 14px;
    font-weight: 500;
    font-size: 30px;
    letter-spacing: 6px;
    text-transform: uppercase;
    color: var(--white);
  }
  .brand__dot {
    width: 18px; height: 18px;
    border-radius: 50%;
    background: var(--green);
    flex: none;
  }
  .brand__services {
    font-size: 11px;
    font-weight: 500;
    letter-spacing: 1.2px;
    color: var(--green);
    text-transform: uppercase;
    border-top: 1px solid var(--grey);
    padding-top: 8px;
  }
  /* Back */
  .card--back {
    background: linear-gradient(120deg, var(--card) 45%, #2a2a2c 75%, var(--card) 100%);
  }
  .contact {
    position: absolute;
    left: 44px;
    top: 36px;
  }
  .contact .brand__name { font-size: 18px; letter-spacing: 4px; gap: 10px; }
  .contact .brand__dot { width: 12px; height: 12px; }
  .contact .brand__services {
    font-size: 8px;
    letter-spacing: .8px;
    margin-top: 8px;
    display: inline-block;
  }
  .person__name {
    margin-top: 22px;
    font-size: 26px;
    font-weight: 700;
    color: var(--green);
  }
  .person__details {
    margin-top: 8px;
    font-size: 13px;
    line-height: 1.4;
    color: var(--white);
  }
  .person__address { margin-top: 12px; font-size: 13px; }
  .contact__list {
    list-style: none;
    margin-top: 10px;
    font-size: 13px;
    line-height: 1.75;
  }
  .contact__list li { display: flex; align-items: center; gap: 10px; }
  .contact__list svg { width: 14px; height: 14px; fill: var(--green); flex: none; }
</style>
</head>
<body>

<section class="card card--front">
  <div class="brand">
    <div class="brand__name"><span class="brand__dot"></span>Crestline Health and Performance</div>
    <div class="brand__services">Physio · S&amp;C · Coaching · Personal Training · Rehab · Recovery</div>
  </div>
  <div class="card__band"></div>
</section>

<section class="card card--back">
  <div class="contact">
    <div class="brand__name"><span class="brand__dot"></span>Crestline Health and Performance</div>
    <div class="brand__services">Physio · S&amp;C · Coaching · Personal Training · Rehab · Recovery</div>

    <h1 class="person__name">Daniel Marlow</h1>
    <p class="person__details">
      Director<br>
      Senior Physiotherapist<br>
      BHlthSc, MPhysioPrac, MExSc(S&amp;C)<br>
      ASCA Level 2
    </p>
    <p class="person__address">12 Linden Rd, Eastvale</p>

    <ul class="contact__list">
      <li>
        <svg viewBox="0 0 24 24"><path d="M6.6 10.8a15.1 15.1 0 0 0 6.6 6.6l2.2-2.2a1 1 0 0 1 1-.25 11.4 11.4 0 0 0 3.6.57 1 1 0 0 1 1 1V20a1 1 0 0 1-1 1A17 17 0 0 1 3 4a1 1 0 0 1 1-1h3.5a1 1 0 0 1 1 1c0 1.25.2 2.45.57 3.57a1 1 0 0 1-.25 1z"/></svg>
        03 5550 1847
      </li>
      <li>
        <svg viewBox="0 0 24 24"><path d="M7 3h8l2 2v4H7zM4 10h16a1 1 0 0 1 1 1v8a1 1 0 0 1-1 1H4a1 1 0 0 1-1-1v-8a1 1 0 0 1 1-1zm3 3v2h4v-2z"/></svg>
        03 5550 2391
      </li>
      <li>
        <svg viewBox="0 0 24 24"><path d="M3 5h18v14H3zm2 2v.5l7 4.5 7-4.5V7l-7 4.5z"/></svg>
        daniel@crestlinehealth.com.au
      </li>
      <li>
        <svg viewBox="0 0 24 24"><path d="M12 2a10 10 0 1 0 0 20 10 10 0 0 0 0-20zm0 2c.9 0 2.2 2 2.7 5H9.3C9.8 6 11.1 4 12 4zM4.3 11h3c-.1 1 0 2 .1 3h-3a8 8 0 0 1-.1-3zm5 0h5.4a16 16 0 0 1 0 3H9.3a16 16 0 0 1 0-3zm7.4 0h3a8 8 0 0 1 0 3h-3c.1-1 .1-2 0-3zM9.3 16h5.4c-.5 2.5-1.8 4-2.7 4s-2.2-1.5-2.7-4z"/></svg>
        www.crestlinehealth.com.au
      </li>
    </ul>
  </div>
  <div class="card__band"></div>
</section>

</body>
</html>
```